Derya & Kerem Wedding Invitation and Decorative Designs

We are looking for a sweet and elegant design for our wedding invitation. We need different versions of the same design to use both as printed hard copies and in digital formats (WhatsApp image, instagram post, etc) Please see attached sample invitation, which we like as a simple and elegant option, but also find it quite basic. We are open to creative suggestions following a similar style.
Once we decide on an invitation design, we would like to use the same design elements in guest name cards, welcome sign, menu cards and print cover for the dance floor of our wedding venue. Please see random samples of these materials attached. We also attach a photo from our wedding venue displaying a close to final visual of the decoration we chose for our wedding day (sharing in case it helps as an inspiration source and helps with matching decoration colors with the designs)
Requirements
Must have
- Must have a style similar to the attached sample invitation

```html
<!DOCTYPE html>
<html lang="tr">
<head>
<meta charset="utf-8">
<title>Derya &amp; Kerem – Düğün Yemeği Davetiyesi</title>
<link href="https://fonts.googleapis.com/css2?family=Montserrat:wght@300;400;700;800&family=Pinyon+Script&family=Cormorant+Garamond:wght@400&display=swap" rel="stylesheet">
<style>
  :root{
    --bg:#e3d8d1;
    --card:#fbfbfa;
    --ink:#1f3a22;
    --ink-soft:#2e3b30;
    --leaf:127,167,132;
    --leaf-deep:63,122,76;
    --wash:156,201,189;
    --wash-light:214,235,229;
    --stain:200,210,208;
    --petal:255,255,255;
    --pollen:214,180,60;
    --rule:#4f7d52;
  }
  *{box-sizing:border-box;margin:0;padding:0}
  html,body{width:1200px;height:1200px;overflow:hidden}
  body{background:var(--bg);font-family:"Montserrat",sans-serif;color:var(--ink-soft);position:relative}

  .invitation{
    position:absolute;left:205px;top:50px;width:790px;height:1100px;
    background:var(--card);overflow:hidden;
    box-shadow:0 6px 24px rgba(80,60,50,.18);
  }

  /* decorative illustration areas – soft fills fading fully inside their boxes */
  .art{position:absolute}
  .art--leaves-top{left:-20px;top:150px;width:300px;height:380px;
    background:radial-gradient(closest-side,rgba(var(--leaf),.5),rgba(var(--leaf),.2) 60%,rgba(var(--leaf),0))}
  .art--wash{left:-120px;top:480px;width:640px;height:720px;
    background:radial-gradient(closest-side,rgba(var(--wash),.7),rgba(var(--wash-light),.45) 60%,rgba(var(--wash-light),0))}
  .art--wash-right{right:-80px;top:420px;width:220px;height:300px;
    background:radial-gradient(closest-side,rgba(var(--stain),.45),rgba(var(--stain),0))}
  .art--leaves-bottom{right:-90px;top:800px;width:400px;height:380px;
    background:radial-gradient(closest-side,rgba(var(--leaf-deep),.55),rgba(var(--leaf),.25) 60%,rgba(var(--leaf),0))}
  .art--flower{left:340px;top:1075px;width:180px;height:80px;
    background:radial-gradient(closest-side,rgba(var(--pollen),.6),rgba(var(--petal),.7) 45%,rgba(var(--petal),0))}

  .content{position:absolute;inset:0;text-align:center}
  .welcome{position:absolute;top:118px;left:0;right:0;font-weight:300;font-size:46px;letter-spacing:3px;color:var(--ink-soft)}
  .welcome-sub{position:absolute;top:180px;left:0;right:0;font-size:19px;letter-spacing:1.5px;color:var(--ink-soft)}
  .name{position:absolute;left:0;right:0;font-family:"Pinyon Script",cursive;color:var(--ink);font-size:100px;line-height:1}
  .name--first{top:250px}
  .amp{position:absolute;top:378px;left:0;right:0;font-family:"Cormorant Garamond",serif;font-size:52px;line-height:1;color:var(--ink-soft)}
  .name--second{top:440px}
  .message{position:absolute;top:585px;left:120px;right:120px;font-size:20px;line-height:1.35}
  .invited{position:absolute;top:650px;left:0;right:0;font-weight:800;font-size:50px;color:var(--ink)}
  .venue{position:absolute;top:735px;left:100px;right:100px;font-size:20px;line-height:1.35}
  .date{position:absolute;top:812px;left:0;right:0;font-weight:800;font-size:26px;color:var(--ink)}

  .schedule{position:absolute;top:875px;left:130px;width:530px;height:150px;display:flex}
  .schedule__item{flex:1;display:flex;flex-direction:column;align-items:center;justify-content:flex-end;gap:22px;border-left:2px solid var(--rule)}
  .schedule__item:first-child{border-left:none}
  .schedule__item svg{width:60px;height:60px;stroke:var(--ink);fill:none;stroke-width:2.4;stroke-linecap:round;stroke-linejoin:round}
  .schedule__time{font-size:26px;color:var(--ink-soft)}

  .rsvp{position:absolute;top:1040px;left:0;right:0;font-weight:800;font-size:26px;color:var(--ink)}
</style>
</head>
<body>
<main class="invitation">
  <div class="art art--leaves-top" role="img" aria-label="Watercolour eucalyptus leaves"></div>
  <div class="art art--wash" role="img" aria-label="Soft mint watercolour wash"></div>
  <div class="art art--wash-right" role="img" aria-label="Faint grey watercolour stain"></div>
  <div class="art art--leaves-bottom" role="img" aria-label="Watercolour green leaves and white blossoms"></div>
  <div class="art art--flower" role="img" aria-label="Watercolour daisy"></div>

  <div class="content">
    <h1 class="welcome">HOŞ GELDİN</h1>
    <p class="welcome-sub">DÜĞÜN YEMEĞİNE</p>
    <p class="name name--first">Derya</p>
    <p class="amp">&amp;</p>
    <p class="name name--second">Kerem</p>
    <p class="message">Bu mutlu günümüzde sizleri de aramızda görmekten mutluluk duyacağız.</p>
    <p class="invited">Davetlisiniz</p>
    <p class="venue">KORULUK BAHÇE: Yalıköy, Çınar Sok. No: 14<br>Sarıyer, İstanbul</p>
    <p class="date">24 ağustos 2024</p>

    <div class="schedule">
      <div class="schedule__item">
        <svg viewBox="0 0 60 60" aria-label="Kokteyl"><path d="M8 18h20l-10 14zM18 32v16M12 48h12"/><path d="M32 16h20l-10 14zM42 30v16M36 46h12"/><path d="M26 8l3 4M34 6v5M40 8l-3 4"/></svg>
        <span class="schedule__time">18.00</span>
      </div>
      <div class="schedule__item">
        <svg viewBox="0 0 60 60" aria-label="Nikah"><circle cx="23" cy="36" r="13"/><circle cx="37" cy="36" r="13"/><path d="M23 19l-4-5h8zM37 19l-4-5h8z"/></svg>
        <span class="schedule__time">19.00</span>
      </div>
      <div class="schedule__item">
        <svg viewBox="0 0 60 60" aria-label="Yemek"><circle cx="30" cy="30" r="20"/><circle cx="30" cy="30" r="13"/><path d="M8 10v16M5 10v8h6v-8M8 26v26M52 10c-5 4-5 14 0 16v26"/></svg>
        <span class="schedule__time">20.00</span>
      </div>
      <div class="schedule__item">
        <svg viewBox="0 0 60 60" aria-label="Kutlama"><path d="M10 52l12-30 18 18z"/><path d="M30 20c2-6 8-8 6-14M38 26c6-2 10 2 14-2M44 10h2M50 18h2M26 8h2"/></svg>
        <span class="schedule__time">00.00</span>
      </div>
    </div>

    <p class="rsvp">LCV: 02160004827</p>
  </div>
</main>
</body>
</html>
```